Business card for massage therapy company called Blue Fern Wellness

Need business card for massage therapy company called Blue Fern Wellness. Would like my logo on the front and the back of the card I have 3 options of logos and you can play with what looks better.

Would like this information displayed on the back of the card:

Marcus Ellery
Licensed Massage Therapist
415-903-2264
bluefern-wellness.example
bluefern_wellness_

```html
<!DOCTYPE html>
<html lang="en">
<head>
<meta charset="utf-8">
<title>Blue Fern Wellness – Business Card</title>
<link href="https://fonts.googleapis.com/css2?family=Montserrat:wght@300;400&family=Allura&display=swap" rel="stylesheet">
<style>
  :root {
    --sage: #6e735d;
    --sage-line: #5f6450;
    --clay: #c59c80;
    --paper: #ffffff;
    --backdrop: #1d1d1d;
  }
  * { box-sizing: border-box; margin: 0; padding: 0; }
  html, body {
    width: 1200px; height: 1015px; overflow: hidden;
    background: var(--backdrop);
    font-family: "Montserrat", sans-serif;
  }
  .sheet {
    width: 1200px; height: 1015px;
    display: flex; flex-direction: column; align-items: center; justify-content: center;
    gap: 60px;
  }
  .card {
    position: relative;
    width: 640px; height: 366px;
    overflow: hidden;
    box-shadow: 0 12px 30px rgba(0,0,0,.55);
  }
  /* Front */
  .card--front {
    background: var(--sage);
    display: flex; align-items: center; justify-content: center;
  }
  .wordmark {
    font-family: "Montserrat", sans-serif;
    font-weight: 300;
    letter-spacing: 0.18em;
    text-transform: uppercase;
    white-space: nowrap;
  }
  .card--front .wordmark { color: var(--paper); font-size: 30px; }

  /* Back */
  .card--back { background: var(--paper); }
  .card--back .panel { position: absolute; inset: 0; }
  .details {
    position: absolute; left: 58px; top: 112px;
    color: var(--paper);
  }
  .details__name {
    font-family: "Allura", cursive;
    font-size: 44px; line-height: 1; font-weight: 400;
  }
  .details__role {
    color: var(--clay);
    font-size: 13px; font-weight: 400;
    margin-top: 6px; letter-spacing: 0.02em;
  }
  .contacts { list-style: none; margin-top: 20px; }
  .contacts li {
    display: flex; align-items: center; gap: 8px;
    font-size: 14px; font-weight: 400; margin-bottom: 7px;
  }
  .contacts svg { width: 20px; height: 20px; flex: none; }
  .card--back .wordmark {
    position: absolute; right: 34px; top: 150px;
    color: var(--sage); font-size: 20px; line-height: 1.5;
    text-align: right;
  }
</style>
</head>
<body>
<main class="sheet">
  <section class="card card--front" aria-label="Card front">
    <span class="wordmark">Blue Fern Wellness</span>
  </section>

  <section class="card card--back" aria-label="Card back">
    <svg class="panel" viewBox="0 0 640 366" aria-hidden="true">
      <circle cx="200" cy="160" r="200" fill="var(--sage)"/>
      <circle cx="208" cy="166" r="204" fill="none" stroke="var(--sage-line)" stroke-width="4"/>
      <circle cx="200" cy="160" r="192" fill="none" stroke="var(--paper)" stroke-width="2" opacity=".85"/>
    </svg>

    <div class="details">
      <h1 class="details__name">Marcus Ellery</h1>
      <p class="details__role">Licensed Massage Therapist</p>
      <ul class="contacts">
        <li>
          <svg viewBox="0 0 20 20" aria-hidden="true"><circle cx="10" cy="10" r="9" fill="none" stroke="var(--clay)" stroke-width="1.2"/><path d="M7 5.5 L8.6 7.6 L7.8 8.8 C8.5 10.3 9.7 11.5 11.2 12.2 L12.4 11.4 L14.5 13 L13.6 14.4 C10 14.2 5.8 10 5.6 6.4 Z" fill="var(--clay)"/></svg>
          415-903-2264
        </li>
        <li>
          <svg viewBox="0 0 20 20" aria-hidden="true"><circle cx="10" cy="10" r="9" fill="none" stroke="var(--clay)" stroke-width="1.2"/><circle cx="10" cy="10" r="5" fill="none" stroke="var(--clay)" stroke-width="1"/><ellipse cx="10" cy="10" rx="2.2" ry="5" fill="none" stroke="var(--clay)" stroke-width="1"/><path d="M5 10 H15" stroke="var(--clay)" stroke-width="1"/></svg>
          bluefern-wellness.example
        </li>
        <li>
          <svg viewBox="0 0 20 20" aria-hidden="true"><circle cx="10" cy="10" r="9" fill="none" stroke="var(--clay)" stroke-width="1.2"/></svg>
          bluefern_wellness_
        </li>
      </ul>
    </div>

    <span class="wordmark">Blue Fern<br>Wellness</span>
  </section>
</main>
</body>
</html>
```